Business Card Design

I need a design/ business card for a new company that caters for Event Hire (decorations and linen only) I am dabbling in rustic/ vintage designs for weddings and would like an elegant look to the cards. Something that will catch peoples eyes amongst the rest of the competitions cards and stand out to all fields, corporate/ weddings and general functions.

I am unsure of colours or pictures i would like so i am open to anything but possibly stick away from photos as i they are not more work of art on the card?
Updates

Target Market(s)

weddings and corporate events

Industry/Entity Type

Business

Contact Information for Business Card

Marlowe Weddings & Event Hire

Servicing the Gladstone Region for Weddings, Corporate & Private Functions

marloweweddings@postvale.net
Phone: 0427 814 253

Requirements
Must have
• The writing "Marlowe Weddings & Event Hire" please
Nice to have
• Something that really stands out as a must have at your event
Should not have
• Pictures that are not of my work

```html
<!DOCTYPE html>
<html lang="en">
<head>
<meta charset="utf-8">
<title>Marlowe Weddings &amp; Event Hire – Business Card</title>
<link rel="stylesheet" href="https://fonts.googleapis.com/css2?family=Quicksand:wght@400;500;600&display=swap">
<style>
  :root {
    --gold: #f0a81c;
    --gold-deep: #e0930f;
    --gold-soft: #f7cf74;
    --cream: #fdf6e6;
    --paper: #ffffff;
    --ink: #2a1b0c;
    --canvas: #ffffff;
  }
  * { box-sizing: border-box; margin: 0; padding: 0; }
  html, body {
    width: 1200px; height: 1200px; overflow: hidden;
    background: var(--canvas);
    font-family: "Quicksand", "Helvetica Neue", Arial, sans-serif;
  }
  .stage { position: relative; width: 1200px; height: 1200px; }

  .card {
    position: absolute; left: 150px;
    width: 900px; height: 515px;
    overflow: hidden;
    background: var(--paper);
    box-shadow: 0 4px 14px rgba(0,0,0,0.12);
  }
  .card--front { top: 60px; }
  .card--back  { top: 625px; }

  .paint-band {
    position: absolute; left: 0; width: 100%;
    background: linear-gradient(100deg, var(--gold) 0%, var(--gold-deep) 35%, var(--gold) 60%, var(--gold-soft) 85%, var(--gold) 100%);
  }
  .paint-wash {
    position: absolute; left: 0; width: 100%;
    background: linear-gradient(95deg, var(--cream) 0%, #fffdf7 40%, var(--cream) 70%, #fbecc8 100%);
  }

  /* Front */
  .card--front .paint-band--top { top: 0; height: 112px; }
  .card--front .paint-wash { top: 112px; height: 255px; }
  .card--front .paint-band--bottom { top: 367px; height: 148px; }
  .front-brand {
    position: absolute; left: 0; right: 0; top: 140px;
    text-align: center;
  }
  .front-brand__name {
    font-weight: 600; font-size: 138px; letter-spacing: 10px;
    color: var(--ink); line-height: 1;
  }
  .front-brand__tagline {
    margin-top: 18px;
    font-weight: 500; font-size: 40px; letter-spacing: 3px;
    color: var(--gold); line-height: 1;
  }

  /* Back */
  .card--back .paint-band--top {
    top: 0; height: 95px;
    background: linear-gradient(180deg, var(--gold) 0%, var(--gold-soft) 70%, var(--cream) 100%);
  }
  .card--back .paint-wash { top: 95px; height: 305px; }
  .card--back .paint-band--bottom { top: 400px; height: 115px; }
  .stripe {
    position: absolute; height: 14px;
    background: linear-gradient(90deg, var(--gold-soft), rgba(247,207,116,0));
  }
  .stripe--left-1 { left: 0; top: 268px; width: 230px; }
  .stripe--left-2 { left: 0; top: 300px; width: 200px; }
  .stripe--right-1 { right: 0; top: 318px; width: 200px; background: linear-gradient(270deg, var(--gold-soft), rgba(247,207,116,0)); }
  .stripe--right-2 { right: 0; top: 352px; width: 230px; background: linear-gradient(270deg, var(--gold-soft), rgba(247,207,116,0)); }

  .back-brand {
    position: absolute; left: 0; right: 0; top: 40px;
    text-align: center;
    font-weight: 600; font-size: 72px; letter-spacing: 6px;
    color: var(--ink); line-height: 1;
  }
  .back-services {
    position: absolute; left: 0; right: 0; top: 148px;
    text-align: center;
    font-weight: 500; font-size: 29px; line-height: 1.35;
    color: var(--ink); letter-spacing: 0.5px;
  }
  .back-contact {
    position: absolute; left: 0; right: 0; top: 262px;
    text-align: center;
    font-weight: 500; font-size: 29px; line-height: 1.4;
    color: var(--ink); letter-spacing: 0.5px;
  }
  .back-contact__label { color: var(--gold); margin-right: 8px; }
</style>
</head>
<body>
<main class="stage">

  <section class="card card--front" aria-label="Business card front">
    <div class="paint-band paint-band--top" role="img" aria-label="Golden brushed paint texture"></div>
    <div class="paint-wash" role="img" aria-label="Soft cream brushed paint texture"></div>
    <div class="paint-band paint-band--bottom" role="img" aria-label="Golden brushed paint texture"></div>
    <div class="front-brand">
      <h1 class="front-brand__name">MARLOWE</h1>
      <p class="front-brand__tagline">WEDDINGS &amp; EVENT HIRE</p>
    </div>
  </section>

  <section class="card card--back" aria-label="Business card back">
    <div class="paint-band paint-band--top" role="img" aria-label="Golden paint texture fading to cream"></div>
    <div class="paint-wash" role="img" aria-label="Soft cream brushed paint texture"></div>
    <div class="paint-band paint-band--bottom" role="img" aria-label="Golden brushed paint texture"></div>
    <span class="stripe stripe--left-1"></span>
    <span class="stripe stripe--left-2"></span>
    <span class="stripe stripe--right-1"></span>
    <span class="stripe stripe--right-2"></span>

    <p class="back-brand">MARLOWE</p>
    <p class="back-services">Servicing the Gladstone Region for<br>Weddings, Corporate &amp; Private Functions</p>
    <p class="back-contact">
      <span class="back-contact__label">P</span>0427 814 253<br>
      <span class="back-contact__label">E</span>marloweweddings@postvale.net
    </p>
  </section>

</main>
</body>
</html>
```